World Class Presentation folder for a National Designer of innovative building products

We are a National Designer, Manufacturer, and distributor of aluminum and stainless Balconies, Railings, Sunshades, and Patio Covers. We sell our products and services to the very best commercial condo and residential builders in the country. This Brochure folder will be the first piece of literature that we give to our customers, and want to WOW them at first glance with a world-class design and look.

We already have a logo and website but would like you to visit https://velmorafabworks.example and view the projects and product information to help inspire you to create an award-winning piece of literature for us.

Besides putting literature in it, the folder must have a place to hold a business card.

Thank you in advance for your great designs, and I look forward to working with you.
Dolan Fratheringe
President | Brennick, OR
418.627.5190 ext 305

```html
<!DOCTYPE html>
<html lang="en">
<head>
<meta charset="utf-8">
<title>Velmora Fabworks — Stationery &amp; Presentation Folder</title>
<link rel="stylesheet" href="https://fonts.googleapis.com/css2?family=Montserrat:wght@400;600;700&family=Open+Sans:wght@400;600&display=swap">
<style>
  :root{
    --red:#c8193c;
    --red-deep:#a3122f;
    --ink:#141414;
    --paper:#ffffff;
    --stage-top:#dddee2;
    --stage-mid:#e8e6e3;
    --text:#555;
    --photo-a:#c9ccc8;
    --photo-b:#e3e4e0;
  }
  *{box-sizing:border-box;margin:0;padding:0}
  html,body{width:1200px;height:3001px;overflow:hidden}
  body{position:relative;font-family:"Open Sans",Arial,sans-serif;color:var(--text)}
  .stage{position:absolute;left:0;width:1200px}
  .stage--stationery{top:0;height:1225px;background:var(--stage-top)}
  .stage--cards{top:1225px;height:930px;background:var(--stage-mid)}
  .stage--folder{top:2155px;height:846px;background:radial-gradient(ellipse at 60% 10%,#fafafa,#d6d7da 75%)}
  .piece{position:absolute;background:var(--paper);box-shadow:0 6px 14px rgba(0,0,0,.18);overflow:hidden}

  .wordmark{font-family:"Montserrat",Arial,sans-serif;font-weight:700;letter-spacing:.04em;text-transform:uppercase;display:flex;align-items:center;gap:.4em;line-height:1}
  .wordmark__dot{display:inline-block;width:.8em;height:.8em;background:currentColor;flex:none}
  .wordmark--red{color:var(--red)}
  .wordmark--white{color:#fff}

  .photo{position:absolute;left:0;width:100%;background:linear-gradient(160deg,var(--photo-a),var(--photo-b) 60%,#d8d2c8)}

  .letterhead{left:210px;top:135px;width:345px;height:485px}
  .letterhead .wordmark{position:absolute;left:30px;top:44px;font-size:13px}
  .letterhead__contact{position:absolute;right:30px;top:36px;font-size:5px;line-height:7px;color:#444}
  .letterhead__body{position:absolute;left:30px;top:112px;width:285px;font-size:5.6px;line-height:9.3px;color:#555;text-align:justify}
  .letterhead__body p{margin-bottom:9px}
  .stripe{position:absolute;left:0;bottom:0;width:100%;height:7px}

  .folder-front{left:590px;top:120px;width:355px;height:505px}
  .folder-band{position:absolute;left:0;width:100%;background:#fff;border-top:5px solid var(--red);border-bottom:5px solid var(--red);display:flex;align-items:center;justify-content:center}

  .envelope-back{left:208px;top:663px;width:377px;height:187px}
  .envelope-back__flap{position:absolute;left:0;top:0;width:100%;height:72px}
  .envelope-back .wordmark{position:absolute;left:0;right:0;top:24px;justify-content:center;font-size:11px}
  .envelope-front{left:207px;top:873px;width:377px;height:187px}
  .envelope-front .wordmark{position:absolute;left:28px;top:28px;font-size:11px}
  .envelope-front__addr{position:absolute;left:28px;top:46px;font-size:5px;color:#444}
  .envelope-front__window{position:absolute;left:28px;top:123px;width:90px;height:41px;border:1px solid #ccc;border-radius:4px;background:#f4f4f5}

  .screen{left:684px;top:700px;width:236px;height:315px;background:linear-gradient(200deg,#2a2a2a,#0b0b0b 55%);display:flex;align-items:center;justify-content:center}
  .screen .wordmark{font-size:15px}

  .card{top:255px;width:460px;height:262px}
  .card--front{left:110px;background:var(--ink);display:flex;flex-direction:column;align-items:center;justify-content:center;gap:22px}
  .card--front .wordmark{font-size:26px}
  .card__url{font-family:"Montserrat",Arial,sans-serif;font-size:11px;letter-spacing:.18em;color:#fff}
  .card__url span{color:var(--red)}
  .card--back{left:630px}
  .card--back .wordmark{position:absolute;left:28px;top:100px;font-size:15px}
  .card__divider{position:absolute;left:215px;top:60px;width:1px;height:118px;background:var(--ink)}
  .card__details{position:absolute;left:232px;top:58px;font-size:10px;line-height:15px;color:#333}
  .card__name{font-family:"Montserrat",Arial,sans-serif;font-weight:700;font-size:14px;color:var(--red);line-height:18px}
  .card__role{font-weight:600;font-size:11px;color:#222}
  .card__line{display:flex;align-items:center;gap:5px}
  .card__line svg{flex:none}
  .card--back .stripe{height:11px;bottom:16px}

  .open-left{left:120px;top:150px;width:470px;height:620px;background:linear-gradient(150deg,#d21c42,var(--red-deep))}
  .open-left .wordmark{position:absolute;left:0;right:0;top:230px;justify-content:center;font-size:28px}
  .open-left__address{position:absolute;left:0;right:0;top:470px;text-align:center;font-family:"Montserrat",Arial,sans-serif;font-size:12px;line-height:17px;color:#fff}
  .open-right{left:590px;top:150px;width:470px;height:620px}
</style>
</head>
<body>

<section class="stage stage--stationery">
  <article class="piece letterhead">
    <div class="wordmark wordmark--red"><span class="wordmark__dot"></span>Velmora Fabworks</div>
    <div class="letterhead__contact">
      1140 Harlow Ridge Ave<br>Brennick, OR 97412<br>418-627-5190<br>418-627-5192<br>info@velmorafabworks.example<br>www.velmorafabworks.example
    </div>
    <div class="letterhead__body">
      <p>Dear customer,</p>
      <p>Lorem ipsum dolor sit amet, consectetur adipisicing elit, sed do eiusmod tempor incididunt ut labore et dolore magna aliqua. Ut enim ad minim veniam, quis nostrud exercitation ullamco laboris nisi ut aliquip ex ea commodo consequat. Duis aute irure dolor in reprehenderit in voluptate velit esse cillum dolore eu fugiat nulla pariatur. Excepteur sint occaecat cupidatat non proident, sunt in culpa qui officia deserunt mollit anim id est laborum.</p>
      <p>Lorem ipsum dolor sit amet, consectetur adipisicing elit, sed do eiusmod tempor incididunt ut labore et dolore magna aliqua. Ut enim ad minim veniam, quis nostrud exercitation ullamco laboris nisi ut aliquip ex ea commodo consequat. Duis aute irure dolor in reprehenderit in voluptate velit esse cillum dolore eu fugiat nulla pariatur. Excepteur sint occaecat cupidatat non proident, sunt in culpa qui officia deserunt mollit anim id est laborum.</p>
      <p>Lorem ipsum dolor sit amet, consectetur adipisicing elit, sed do eiusmod tempor incididunt ut labore et dolore magna aliqua. Ut enim ad minim veniam, quis nostrud exercitation ullamco laboris nisi ut aliquip ex ea commodo consequat. Duis aute irure dolor in reprehenderit in voluptate velit esse cillum dolore eu fugiat nulla pariatur. Excepteur sint occaecat cupidatat non proident, sunt in culpa qui officia deserunt mollit anim id est laborum.</p>
      <p>Lorem ipsum dolor sit amet, consectetur adipisicing elit, sed do eiusmod tempor incididunt ut labore et dolore magna aliqua. Ut enim ad minim veniam, quis nostrud exercitation ullamco laboris nisi ut aliquip ex ea commodo consequat. Duis aute irure dolor in reprehenderit.</p>
      <p>Yours Sincerely,</p>
    </div>
    <svg class="stripe" viewBox="0 0 345 7" preserveAspectRatio="none"><polygon points="0,0 232,0 225,7 0,7" fill="var(--red)"/><polygon points="236,0 345,0 345,7 229,7" fill="var(--ink)"/></svg>
  </article>

  <article class="piece folder-front">
    <div class="photo" style="top:0;height:185px" role="img" aria-label="Faded photo of a modern condo building with aluminum balconies and railings"></div>
    <div class="folder-band" style="top:180px;height:170px">
      <div class="wordmark wordmark--red" style="font-size:22px"><span class="wordmark__dot"></span>Velmora Fabworks</div>
    </div>
    <div class="photo" style="top:350px;height:155px" role="img" aria-label="Faded photo of a patio with outdoor seating behind a metal railing"></div>
  </article>

  <article class="piece envelope-back">
    <svg class="envelope-back__flap" viewBox="0 0 377 72" preserveAspectRatio="none"><path d="M0 0H377V40Q377 58 359 60L30 70Q0 72 0 44Z" fill="var(--ink)"/></svg>
    <div class="wordmark wordmark--white"><span class="wordmark__dot" style="color:var(--red)"></span>Velmora Fabworks</div>
  </article>

  <article class="piece envelope-front">
    <div class="wordmark wordmark--red"><span class="wordmark__dot"></span>Velmora Fabworks</div>
    <div class="envelope-front__addr">1140 Harlow Ridge Ave Brennick, OR 97412</div>
    <div class="envelope-front__window"></div>
  </article>

  <article class="piece screen">
    <div class="wordmark wordmark--white"><span class="wordmark__dot" style="color:var(--red)"></span>Velmora Fabworks</div>
  </article>
</section>

<section class="stage stage--cards">
  <article class="piece card card--front">
    <div class="wordmark wordmark--white"><span class="wordmark__dot" style="color:var(--red)"></span>Velmora Fabworks</div>
    <div class="card__url">www.<span>velmorafabworks</span>.example</div>
  </article>

  <article class="piece card card--back">
    <div class="wordmark wordmark--red"><span class="wordmark__dot"></span>Velmora<br>Fabworks</div>
    <div class="card__divider"></div>
    <div class="card__details">
      <div class="card__name">Dolan Fratheringe</div>
      <div class="card__role">President | Brennick, OR</div>
      <div>1140 Harlow Ridge Ave</div>
      <div>Brennick, OR 97412</div>
      <div class="card__line"><svg width="9" height="9" viewBox="0 0 10 10"><path d="M2 0L4 3 3 4Q4 6 6 7L7 6 10 8 8 10Q2 9 0 2Z" fill="var(--red)"/></svg>418-627-5190</div>
      <div class="card__line"><svg width="9" height="9" viewBox="0 0 10 10"><rect x="1" y="3" width="8" height="6" fill="var(--red)"/><rect x="3" y="0" width="4" height="3" fill="var(--red)"/></svg>418-627-5192</div>
      <div class="card__line"><svg width="9" height="9" viewBox="0 0 10 10"><rect y="2" width="10" height="7" fill="var(--red)"/><path d="M0 2L5 6 10 2" stroke="#fff" fill="none"/></svg>info@velmorafabworks.example</div>
      <div class="card__line"><svg width="9" height="9" viewBox="0 0 10 10"><circle cx="5" cy="5" r="5" fill="var(--red)"/></svg>www.velmorafabworks.example</div>
    </div>
    <svg class="stripe" viewBox="0 0 460 11" preserveAspectRatio="none"><polygon points="0,0 345,0 337,11 0,11" fill="var(--red)"/><polygon points="349,0 460,0 460,11 341,11" fill="var(--ink)"/></svg>
  </article>
</section>

<section class="stage stage--folder">
  <article class="piece open-left">
    <div class="wordmark wordmark--white"><span class="wordmark__dot"></span>Velmora Fabworks</div>
    <div class="open-left__address">
      Velmora Fabworks<br>1140 Harlow Ridge Ave<br>Brennick, OR 97412<br>P : 418-627-5190 &nbsp;P : 800-555-0147<br>F : 418-627-5192
    </div>
  </article>
  <article class="piece open-right">
    <div class="photo" style="top:0;height:215px" role="img" aria-label="Faded photo of a modern condo building with aluminum balconies and railings"></div>
    <div class="folder-band" style="top:210px;height:200px">
      <div class="wordmark wordmark--red" style="font-size:28px"><span class="wordmark__dot"></span>Velmora Fabworks</div>
    </div>
    <div class="photo" style="top:410px;height:210px" role="img" aria-label="Faded photo of a patio with outdoor seating behind a metal railing"></div>
  </article>
</section>

</body>
</html>
```